Copper Vale Tattoo

Business card / Appointment card in one

Ive attached the new logo along with a simple format of what I would like written out on the back! Would like a clean/ modern style font to be used! I also attached the current card for a reference of style!

The colors of this would be either white and gold lettering or black with gold lettering.

Email - CopperValeNB@inkmail.example
Ph # 555-482-9073

The message at bottom of back - All cancellations or No Call No Shows within 48 hours of appointment time will result in a forfeit of deposit.

Small block avail (if card is black) to write in appointment date/time

Target Market(s)

Card for Tattoo shop

Contact Information for Business Card

in project description area!

Font styles to use
Sans Serif

Requirements
Must have
• Please refer to current business card photos that were attached as well!
Nice to have
• Looking for blacks, greys and gold for color scheme

```html
<!DOCTYPE html>
<html lang="en">
<head>
<meta charset="utf-8">
<title>Copper Vale Tattoo – Appointment Card</title>
<link rel="stylesheet" href="https://fonts.googleapis.com/css2?family=Roboto:wght@400;500&family=Work+Sans:wght@400&display=swap">
<style>
  :root {
    --backdrop: #262626;
    --card-light: #dcdcdc;
    --card-dark: #1e1e1e;
    --gold: #b08d3a;
    --silver: #a9a9a9;
  }
  * { box-sizing: border-box; margin: 0; padding: 0; }
  html, body {
    width: 1200px; height: 897px; overflow: hidden;
    background: var(--backdrop);
  }
  .canvas { position: relative; width: 1200px; height: 897px; }
  .card {
    position: absolute; left: 303px; width: 595px; height: 338px;
    box-shadow: 0 4px 14px rgba(0,0,0,.45);
  }
  .card--appointment {
    top: 92px; background: var(--card-light); color: var(--gold);
    font-family: "Work Sans", sans-serif; text-align: center;
  }
  .card--brand { top: 470px; background: var(--card-dark); }

  .contact {
    position: absolute; top: 27px; left: 0; right: 0;
    font-family: "Roboto", sans-serif; font-weight: 500;
    font-size: 18px; line-height: 24px; letter-spacing: .5px;
  }
  .appointment-heading {
    position: absolute; top: 140px; left: 0; right: 0; font-size: 17px;
    letter-spacing: .5px;
  }
  .date-time {
    position: absolute; top: 191px; left: 31px; right: 31px;
    display: flex; font-size: 14px; align-items: flex-end;
  }
  .date-time .blank {
    flex: 1; border-bottom: 1px solid var(--gold); height: 14px; margin-right: 1px;
  }
  .weekdays {
    position: absolute; top: 233px; left: 31px; right: 31px;
    display: flex; justify-content: space-between; font-size: 18px;
  }
  .weekday { display: flex; align-items: center; gap: 6px; }
  .weekday .box {
    width: 12px; height: 12px; border: 2px solid var(--gold);
  }
  .policy {
    position: absolute; top: 268px; left: 40px; right: 40px;
    font-size: 15px; line-height: 21px; letter-spacing: .3px;
  }

  .brand-name {
    position: absolute; inset: 0;
    display: flex; align-items: center; justify-content: center; gap: 12px;
    font-family: "Work Sans", sans-serif; font-size: 26px;
    color: var(--silver); letter-spacing: 1px;
  }
  .brand-name .mark {
    width: 14px; height: 14px; border-radius: 50%; background: var(--silver);
  }
</style>
</head>
<body>
<main class="canvas">
  <section class="card card--appointment">
    <div class="contact">
      <p>E : CopperValeNB@inkmail.example</p>
      <p>P : 555-482-9073</p>
    </div>
    <p class="appointment-heading">Appointment on:</p>
    <div class="date-time">
      <span>Date,</span><span class="blank"></span>
      <span>Time,</span><span class="blank"></span>
    </div>
    <div class="weekdays">
      <span class="weekday"><span class="box"></span>Mon.</span>
      <span class="weekday"><span class="box"></span>Tues.</span>
      <span class="weekday"><span class="box"></span>Wed.</span>
      <span class="weekday"><span class="box"></span>Thurs.</span>
      <span class="weekday"><span class="box"></span>Fri.</span>
      <span class="weekday"><span class="box"></span>Sat.</span>
    </div>
    <p class="policy">All cancellations or No Call No Shows within 48 hours of Appointment time will result in a forfeit of deposit.</p>
  </section>

  <section class="card card--brand">
    <div class="brand-name"><span class="mark"></span>Copper Vale Tattoo</div>
  </section>
</main>
</body>
</html>
```